Harbor Ridge Elementary School Letterhead

We would like a letterhead that includes our school mascot (Flicker the Falcon), school address, and phone number. We want something with personality and a little fun. Our school colors are navy blue, green (like the flag in our graphic), and gray. We included an example of a letterhead we like the feel of (on the fun side). The example is the image titled "sample." We are the Harbor Ridge Falcons.
Harbor Ridge Elementary
Address: 418 Marlow Fern, Irvine, CA 92781
Phone: (949) 555-0174
harborridge.oksd.example
Target Market(s)
Elementary School Families

```html
<!DOCTYPE html>
<html lang="en">
<head>
<meta charset="utf-8">
<title>Harbor Ridge Elementary Letterhead</title>
<link href="https://fonts.googleapis.com/css2?family=Montserrat:wght@400;500;600;700;800&family=Mrs+Saint+Delafield&display=swap" rel="stylesheet">
<style>
  :root {
    --backdrop: #e6e7e9;
    --paper: #ffffff;
    --navy: #264d9b;
    --navy-ink: #1f3f6e;
    --periwinkle: #8797c5;
    --ink: #2b2b2b;
    --muted: #8a8a8a;
    --accent-red: #e0332f;
    --mascot-gray: #9a9a9a;
    --flag-green: #2f9a45;
  }
  * { box-sizing: border-box; margin: 0; padding: 0; }
  html, body { width: 1200px; height: 1200px; overflow: hidden; }
  body {
    background: var(--backdrop);
    font-family: "Montserrat", sans-serif;
    position: relative;
  }
  .letterhead {
    position: absolute;
    left: 175px; top: 50px;
    width: 850px; height: 1100px;
    background: var(--paper);
    box-shadow: 0 6px 24px rgba(0,0,0,0.12);
    overflow: hidden;
  }
  .brand {
    position: absolute; left: 62px; top: 62px;
    display: flex; align-items: center; gap: 14px;
  }
  .brand-dot {
    width: 46px; height: 46px; border-radius: 50%;
    background: var(--navy);
  }
  .brand-name {
    font-weight: 800; font-size: 40px; color: var(--navy);
    letter-spacing: 1px; text-transform: uppercase;
  }
  .date-line {
    position: absolute; right: 70px; top: 170px;
    font-size: 12px; color: var(--ink);
  }
  .date-line .label { color: var(--accent-red); font-weight: 600; }
  .recipient {
    position: absolute; left: 62px; top: 215px;
    font-size: 12px; color: var(--ink); line-height: 1.35;
  }
  .recipient .to { font-size: 11px; color: var(--muted); }
  .recipient .name { font-size: 16px; font-weight: 700; color: var(--navy-ink); }
  .recipient .web b { font-weight: 700; }
  .letter-body {
    position: absolute; left: 62px; top: 315px; width: 700px;
    font-size: 11px; line-height: 1.45;
  }
  .letter-body p { margin-bottom: 12px; }
  .letter-body .soft { color: var(--muted); }
  .letter-body .strong { color: var(--ink); font-weight: 500; }
  .signature {
    position: absolute; left: 190px; top: 800px; width: 230px;
    text-align: center;
  }
  .signature .script {
    font-family: "Mrs Saint Delafield", cursive;
    font-size: 40px; color: var(--ink); line-height: 1;
  }
  .signature .rule { border-top: 1.5px solid var(--ink); margin-top: 4px; }
  .signature .role {
    font-size: 10px; letter-spacing: 0.5px; color: var(--ink);
    margin-top: 8px; text-transform: uppercase;
  }
  .mascot-art {
    position: absolute; right: 80px; top: 805px;
    width: 125px; height: 125px; border-radius: 18px;
    background: radial-gradient(circle at 40% 55%, #c9c9c9, var(--mascot-gray) 70%);
  }
  .mascot-flag {
    position: absolute; right: 62px; top: 785px;
    width: 50px; height: 30px; border-radius: 4px;
    background: var(--flag-green);
  }
  .footer-band { position: absolute; left: 0; bottom: 0; width: 850px; height: 160px; }
  .footer-school {
    position: absolute; left: 62px; bottom: 60px; color: #fff;
  }
  .footer-school .title {
    font-weight: 700; font-size: 26px; font-variant: small-caps; letter-spacing: 1.5px;
  }
  .footer-school .address { font-size: 14px; margin-top: 6px; }
  .footer-contact {
    position: absolute; left: 600px; bottom: 52px; color: #fff;
    font-size: 13px; line-height: 1.75;
  }
  .footer-contact li { list-style: none; display: flex; align-items: center; gap: 10px; }
  .footer-contact svg { width: 13px; height: 13px; fill: #fff; flex: none; }
</style>
</head>
<body>
  <main class="letterhead">
    <div class="brand">
      <span class="brand-dot"></span>
      <span class="brand-name">Harbor Ridge</span>
    </div>

    <div class="date-line"><span class="label">Date:</span> 24-03-2018</div>

    <div class="recipient">
      <div class="to">To</div>
      <div class="name">Alan Reyes</div>
      <div>CEO, NORTHLEAF STUDIO</div>
      <div class="web"><b>W:</b> www.northleafstudio.example</div>
    </div>

    <section class="letter-body">
      <p class="soft">Lorem ipsum dolor sit amet, consectetur adipiscing elit. Pellentesque dictum, ante non ullamcorper convallis, nunc quam blandit metus, ac mollis eros felis a orci. Donec congue, mauris ut pulvinar lobortis, dolor massa feugiat nisi, at tincidunt metus leo vel elit. Proin facilisis semper lobortis. Vivamus augue purus, cursus quis urna non, accumsan pellentesque est. Nulla in iaculis magna, quis aliqu et ex. Cras efficitur metus eget purus euismod facilisis. Proin non metus tincidunt, auctor ipsum a, tempor mi.</p>
      <p class="strong">Nulla egestas vulputate risus, ut vestibulum diam commodo id. Mauris ornare libero eu erat porttitor ultrices. Proin sed lectus scelerisque ligula bibendum sagittis ac nec leo. Donec ac accumsan diam, et lobortis mauris.</p>
      <p class="strong">Nulla congue volutpat nisl ac lobortis. Integer dignissim interdum libero, quis feugiat velit pretium at. Phasellus sit amet libero rutrum, feugiat odio et, tempus purus. Cras ultricies, leo at fringilla sollicitudin, leo sapien placerat enim, a rutrum lorem enim ut tortor. Phasellus magna ante, congue maximus egestas sit amet, venenatis scelerisque felis.</p>
      <p class="soft">Nulla congue volutpat nisl ac lobortis. Integer dignissim interdum libero, quis feugiat velit pretium at. Phasellus sit amet libero rutrum, feugiat odio et, tempus purus. Cras ultricies, leo at fringilla sollicitudin, leo sapien placerat enim, a rutrum lorem enim ut tortor. Phasellus magna ante, congue maximus egestas sit amet, venenatis scelerisque felis.</p>
      <p class="soft">Curabitur vitae urna volutpat, varius velit vehicula, fermentum magna. In maximus metus nunc, nec aliquet justo commodo eget. Nullam rhoncus vehicula gravida. Maecenas non sem at erat lacinia convallis. Aliquam at lobortis erat.</p>
      <p class="soft">Nulla congue volutpat nisl ac lobortis. Integer dignissim interdum libero, quis feugiat velit pretium at. Phasellus sit amet libero rutrum, feugiat odio et, tempus purus. Cras ultricies, leo at fringilla sollicitudin, leo sapien placerat enim, a rutrum lorem enim ut tortor. Phasellus magna ante, congue maximus egestas sit amet, venenatis scelerisque felis.</p>
    </section>

    <div class="signature">
      <div class="script">Lena Ortiz</div>
      <div class="rule"></div>
      <div class="role">Designation place here</div>
    </div>

    <div class="mascot-flag" role="img" aria-label="Green school flag held by the mascot"></div>
    <div class="mascot-art" role="img" aria-label="Flicker the Falcon mascot illustration waving"></div>

    <svg class="footer-band" viewBox="0 0 850 160" preserveAspectRatio="none" aria-hidden="true">
      <rect x="0" y="0" width="850" height="160" fill="var(--periwinkle)"/>
      <polygon points="0,0 545,0 435,160 0,160" fill="var(--navy)"/>
    </svg>

    <div class="footer-school">
      <div class="title">Harbor Ridge Elementary</div>
      <div class="address">418 Marlow Fern, Irvine, CA 92781</div>
    </div>

    <ul class="footer-contact">
      <li><svg viewBox="0 0 24 24"><path d="M6.6 10.8a15 15 0 0 0 6.6 6.6l2.2-2.2a1 1 0 0 1 1-.25 11.4 11.4 0 0 0 3.6.57 1 1 0 0 1 1 1V20a1 1 0 0 1-1 1A17 17 0 0 1 3 4a1 1 0 0 1 1-1h3.5a1 1 0 0 1 1 1c0 1.25.2 2.45.57 3.570a1 1 0 0 1-.25 1z"/></svg>(949) 555-0174</li>
      <li><svg viewBox="0 0 24 24"><path d="M2 5h20v14H2z M2 5l10 8 10-8" fill="none" stroke="#fff" stroke-width="2"/></svg>info@harborridge.oksd.example</li>
      <li><svg viewBox="0 0 24 24"><circle cx="12" cy="12" r="9" fill="none" stroke="#fff" stroke-width="2"/><path d="M3 12h18M12 3c3 3 3 15 0 18M12 3c-3 3-3 15 0 18" fill="none" stroke="#fff" stroke-width="1.6"/></svg>www.harborridge.oksd.example</li>
    </ul>
  </main>
</body>
</html>
```